Selbsthilfegruppe für organtransplantierte Personen sucht Flyer-Design
Sehr schnelle Reaktion auf Änderungswünsche und top Support bis zum Druck :) Gerne wieder!
Zielgruppe
Wir sind eine Selbsthilfegruppe für organtransplantierte Personen, Zielgruppe sind Personen aus der Region die auch ein Spenderorgan empfangen haben und deren Angehörige, die Beistand und Information suchen sowie gemeinsame Aktivitäten wahrnehmen möchten.
Aufgabenstellung
Es gibt bereits einen Flyer der jedoch überarbeitet und etwas schöner und moderner gestaltet werden soll. Der Text kann bestehen bleiben und die Aufteilung muss nicht zwingend geändert werden, anstelle der aktuellen Fotos sollen dann andere eingefügt werden, die übergeben werden, sobald das Design akzeptiert wurde. Es geht hauptsächlich um das Design selbst, es soll ansprechen, freundlich, modern und hoffnungsvoll sein, die Grundfarbe sollte grün sein. Das Logo kann beibehalten aber farblich auch gerne angepasst werden. Es soll ein normaler Faltflyer sein, 2 Faltungen und damit vorn und hinten je 3 einzelne Bereiche wie aktuell, Gesamtmaß A4. Bei Rückfragen gerne melden!

```html
<!DOCTYPE html>
<html lang="de">
<head>
<meta charset="utf-8">
<title>Flyer – Selbsthilfegruppe für Organtransplantation</title>
<link href="https://fonts.googleapis.com/css2?family=Quicksand:wght@500;600;700&family=Pinyon+Script&display=swap" rel="stylesheet">
<style>
  :root{
    --stage:#a9aaac;
    --paper:#ffffff;
    --orange:#d98f1f;
    --amber:#e3a02a;
    --green:#5b9a37;
    --green-dark:#4d8c2f;
    --white:#ffffff;
  }
  html,body{margin:0;padding:0;overflow:hidden}
  body{width:1200px;height:675px;background:radial-gradient(circle at 50% 50%,#c9cacc 0%,var(--stage) 100%);position:relative;font-family:"Quicksand",sans-serif}
  .flyer{position:absolute;left:134px;top:7px;width:933px;height:660px;background:var(--paper);overflow:hidden;box-shadow:0 4px 10px rgba(0,0,0,.25)}
  .flyer__shapes{position:absolute;inset:0}
  .photo{position:absolute;border:3px solid var(--green);border-radius:12px;box-sizing:border-box}
  .photo--event{left:320px;top:87px;width:277px;height:160px;background:linear-gradient(135deg,#b9a07a 0%,#7a9a55 45%,#3f8a3a 60%,#c9b9a0 100%)}
  .photo--group{left:622px;top:244px;width:311px;height:260px;border-radius:12px 12px 0 0;background:linear-gradient(180deg,#e8dcc0 0%,#d9c9a8 40%,#9a6a6a 65%,#c0506a 80%,#8a7a80 100%)}
  .benefits{position:absolute;left:0;top:0;margin:0;padding:0;list-style:none}
  .benefits li,.supporters li{position:absolute;transform:translateY(-50%);color:var(--orange);font-size:15px;font-weight:500;line-height:19px;white-space:nowrap}
  .benefits li{left:39px}
  .benefits li::before,.supporters li::before{content:"";position:absolute;left:-13px;top:50%;width:10px;height:10px;margin-top:-5px;border-radius:50%;background:var(--green)}
  .contact-title{position:absolute;left:409px;top:58px;transform:translate(-50%,-50%);font-family:"Pinyon Script",cursive;font-size:36px;color:var(--orange);border-bottom:1px solid var(--orange);line-height:38px;padding:0 2px}
  .contact-heading{position:absolute;left:320px;top:258px;margin:0;color:var(--orange);font-size:15.5px;font-weight:700;border-bottom:1.5px solid var(--orange);padding-bottom:3px}
  .contact-intro{position:absolute;left:332px;top:306px;transform:translateY(-50%);margin:0;color:var(--orange);font-size:15.5px;font-weight:500}
  .supporters{position:absolute;left:0;top:0;margin:0;padding:0;list-style:none}
  .supporters li{left:332px;font-size:15.5px;line-height:20px}
  .brand{position:absolute;left:622px;width:311px;top:0;text-align:center}
  .brand__mark{width:26px;height:26px;border-radius:50%;background:var(--green);margin:52px auto 0}
  .brand__name{margin:20px 0 0;color:var(--orange);font-size:28px;font-weight:600;line-height:32px;border-bottom:1px solid var(--orange);display:inline-block;padding:0 6px}
  .brand__tagline{margin:8px 0 0;color:var(--orange);font-size:16px;font-weight:500;line-height:20px}
  .offer{position:absolute;left:622px;width:311px;top:550px;text-align:center;color:var(--white);font-size:19px;font-weight:500;line-height:24px;margin:0}
</style>
</head>
<body>
<main class="flyer">
  <div class="photo photo--group" role="img" aria-label="Gruppenfoto der Selbsthilfegruppe in einem Gemeinschaftsraum"></div>
  <svg class="flyer__shapes" width="933" height="660" viewBox="0 0 933 660" aria-hidden="true">
    <defs>
      <linearGradient id="swoosh" x1="0" y1="0" x2="1" y2="0">
        <stop offset="0" stop-color="#e3a02a"/>
        <stop offset="0.55" stop-color="#8aa836"/>
        <stop offset="1" stop-color="#5b9a37"/>
      </linearGradient>
      <linearGradient id="band" x1="0" y1="0" x2="1" y2="0">
        <stop offset="0" stop-color="#5b9a37"/>
        <stop offset="0.6" stop-color="#6a9e36"/>
        <stop offset="1" stop-color="#d9a02c"/>
      </linearGradient>
    </defs>
    <path d="M0 0 L435 0 C300 28 110 70 0 121 Z" fill="url(#swoosh)"/>
    <rect x="622" y="463" width="311" height="197" fill="#5b9a37"/>
    <path d="M0 602 Q450 555 622 518 Q800 475 933 421 L933 660 L0 660 Z" fill="url(#band)"/>
    <path d="M622 518 Q800 475 933 421" fill="none" stroke="#fff" stroke-width="2"/>
  </svg>

  <ul class="benefits">
    <li style="top:139px">Suchen und Finden von<br>Gleichgesinnten</li>
    <li style="top:193px">Einsamkeit durch Gemeinsamkeit<br>überwinden</li>
    <li style="top:240px">Lebenssituation verbessern</li>
    <li style="top:287px">Beziehungen aufbauen<br>und verbessern</li>
    <li style="top:343px">Schwierigkeiten zusammen<br>meistern</li>
    <li style="top:389px">Teilnehmen und verstehen</li>
    <li style="top:426px">Handeln in eigener Sache</li>
    <li style="top:464px">Informationen geben</li>
    <li style="top:501px">Lösungen entdecken und entwickeln</li>
    <li style="top:547px">Freude am Leben finden:<br>Jetzt erst recht!</li>
  </ul>

  <div class="contact-title">Kontakt:</div>
  <div class="photo photo--event" role="img" aria-label="Foto einer Ansprechpartnerin am Infostand auf einem Marktplatz"></div>
  <h2 class="contact-heading">Info zum Ansprechpartner:</h2>
  <p class="contact-intro">Wir werden unterstützt</p>
  <ul class="supporters">
    <li style="top:356px">von der Stiftung Lebensbrücke<br>(SLB)</li>
    <li style="top:406px">vom Klinikum Talbach: GIZ</li>
    <li style="top:456px">von Fachärzten aus dem Bereich<br>Innere Medizin</li>
    <li style="top:515px">vom Frauenzentrum „Marlene“<br>in Talbach</li>
  </ul>

  <header class="brand">
    <div class="brand__mark"></div>
    <h1 class="brand__name">Miteinander stark</h1>
    <p class="brand__tagline">Selbsthilfegruppe<br>für Organtransplatation</p>
  </header>

  <p class="offer">Wir bieten Hilfe für Betroffene<br>sowie Angehörige im Raum<br>Talbach an.</p>
</main>
</body>
</html>
```